TRENDY & MODERN BUSINESS CARD DESIGN for Media Company *

I need a minimalistic - clean - modern and professional business card layout and design for MEDIA & PHOTOGRAPHY STUDIO.

We do NOT have a logo, and not really looking for one - but rather excellent typography and design. We would consider the 3 as a focal point.

We do personal and commercial photography.

Target Market(s)

Personal and commercial photography clientele

Contact Information for Business Card

ZUB size - from zub.com / size guidelines are enclosed in the brief

Font styles to use
Sans Serif

Colors
f78f20
eda3c7
cee9f5
0555a3
e667a6
fbf289

Requirements
Must have
• Clean lines - Modern layout
Nice to have
• All blue background as an option - use color palette in brief please.
Should not have
• Old fashion fonts and regular fonts.

```html
<!DOCTYPE html>
<html lang="en">
<head>
<meta charset="utf-8">
<title>Ninth Lens Media – Business Card</title>
<link rel="stylesheet" href="https://fonts.googleapis.com/css2?family=Saira+Condensed:wght@600;700&family=Raleway:wght@300&display=swap">
<style>
  :root {
    --orange: #f78f20;
    --ink: #333333;
    --black: #1c1c1c;
    --paper: #ffffff;
    --backdrop: #e5e5e5;
  }
  * { margin: 0; padding: 0; box-sizing: border-box; }
  html, body { width: 1200px; height: 1200px; overflow: hidden; background: var(--backdrop); }
  .card {
    position: absolute; left: 286px; width: 642px; height: 430px;
    background: var(--paper); border: 1px solid #555;
    box-shadow: 0 8px 18px rgba(0,0,0,0.25);
    overflow: hidden;
  }
  .card--front { top: 123px; }
  .card--back { top: 633px; }
  .bands { position: absolute; left: 0; top: 0; width: 642px; height: 430px; }
  .text { position: absolute; white-space: nowrap; line-height: 1; }
  .display { font-family: "Saira Condensed", sans-serif; font-weight: 700; }

  .brand { color: var(--orange); letter-spacing: 0.5px; }
  .front-brand { left: 0; width: 642px; text-align: center; top: 148px; font-size: 62px; }
  .front-tagline { left: 0; width: 642px; text-align: center; top: 218px; font-size: 33px; color: var(--ink); }
  .services {
    left: 154px; width: 333px; top: 321px; text-align: center;
    font-family: "Raleway", sans-serif; font-weight: 300; font-size: 15px;
    color: var(--paper); line-height: 22px;
  }
  .services .dot { margin: 0 6px; }

  .back-brand { left: 26px; top: 190px; font-size: 27px; }
  .person-name { right: 59px; top: 36px; font-size: 42px; color: var(--black); letter-spacing: 0.5px; }
  .person-name .surname { color: var(--orange); }
  .person-role { right: 60px; top: 80px; font-size: 16px; color: var(--black); font-weight: 600; letter-spacing: 0.3px; }
  .contact { left: 341px; color: var(--black); }
  .contact--email { top: 122px; font-size: 24px; }
  .contact--phone { top: 180px; font-size: 24px; }
  .contact--address { top: 241px; font-size: 12px; line-height: 14px; font-weight: 600; }
  .icon { position: absolute; left: 245px; width: 26px; height: 26px; fill: var(--orange); }
  .icon--email { top: 124px; }
  .icon--phone { top: 182px; }
  .icon--pin { top: 240px; }
  .back-tagline { left: 64px; top: 325px; font-size: 33px; color: var(--paper); }
</style>
</head>
<body>

<section class="card card--front">
  <svg class="bands" viewBox="0 0 642 430" aria-hidden="true">
    <polygon points="0,316 129,316 167,370 0,370" fill="var(--ink)"/>
    <polygon points="154,316 487,316 450,370 192,370" fill="var(--orange)"/>
    <polygon points="512,316 642,316 642,370 475,370" fill="var(--ink)"/>
  </svg>
  <div class="text display brand front-brand">NINTH LENS MEDIA</div>
  <div class="text display front-tagline">Framing Moments. Making Art.</div>
  <div class="text services">
    Studio<span class="dot">•</span>Portrait<span class="dot">•</span><br>
    Events<span class="dot">•</span>Commercial<span class="dot">•</span>Travel
  </div>
</section>

<section class="card card--back">
  <svg class="bands" viewBox="0 0 642 430" aria-hidden="true">
    <polygon points="0,317 486,317 448,370 0,370" fill="var(--orange)"/>
    <polygon points="512,317 642,317 642,370 474,370" fill="var(--ink)"/>
  </svg>
  <div class="text display brand back-brand">NINTH LENS MEDIA</div>

  <div class="text display person-name">Marisol <span class="surname">Vega</span></div>
  <div class="text display person-role">Founder &amp; Media Director</div>

  <svg class="icon icon--email" viewBox="0 0 24 24" aria-hidden="true">
    <path d="M12 1 1 8v14h22V8zM3 20V10.5l6.5 4.8L3 20zm2-0.5 6-4.4 1 .7 1-.7 6 4.4zm16 .5-6.5-4.7L21 10.5z"/>
  </svg>
  <div class="text display contact contact--email">mari@ninthlensmedia.com</div>

  <svg class="icon icon--phone" viewBox="0 0 24 24" aria-hidden="true">
    <path d="M6.6 2 3 3.2C2.4 8.5 6 15.8 12.6 20.2c2.6 1.7 5.3 2.1 7.2 1.6l1.5-3.4-4.6-3.2-2.5 1.8c-2.7-1.5-5-4.3-6-7l2.2-2.1z"/>
  </svg>
  <div class="text display contact contact--phone">(305) 555-0142</div>

  <svg class="icon icon--pin" viewBox="0 0 24 24" aria-hidden="true">
    <path d="M12 1a8 8 0 0 0-8 8c0 5.5 8 14 8 14s8-8.5 8-14a8 8 0 0 0-8-8zm0 11.5a3.5 3.5 0 1 1 0-7 3.5 3.5 0 0 1 0 7z"/>
  </svg>
  <div class="text display contact contact--address">2040 Harbor Avenue, 8 th Floor<br>Miami, FL 33130</div>

  <div class="text display back-tagline">Framing Moments. Making Art.</div>
</section>

</body>
</html>
```